Business Card Design

I'm a commercial general contractor remodel offices, hotels, health clubs and stores mostly San Francisco and the peninsula
the file I down loaded is kind of what I want I like the I beam with my company name in it, that would be fine with me but if you have better Idea will look at it you never know, I'm decided to give in and change my company name to how every one knows me, I have been in business since 1991, I like the I beam logo I included one of my old card from my old company for reference for you.

Industry/Entity Type

Business

Contact Information for Business Card

BRAVO CONSTRUCTION (is my company name)
Reginald Pottle contractor, LIc 384217
4318 Quarry Lane, San Bruno, California 94066
mobile, (415) 555-0147
phone (650) 555-0183
Fax, (650) 555-0184
email, bravo@bravoconstruction.example

```html
<!DOCTYPE html>
<html lang="en">
<head>
<meta charset="utf-8">
<title>Bravo Construction — Business Card</title>
<link rel="stylesheet" href="https://fonts.googleapis.com/css2?family=Caladea&display=swap">
<style>
  :root {
    --card-bg: #a4bcc3;
    --accent-blue: #1ca8ff;
    --name-blue: #1673b8;
    --ink: #253238;
  }
  html, body {
    margin: 0;
    padding: 0;
    overflow: hidden;
    background: var(--card-bg);
  }
  .card {
    position: relative;
    width: 1200px;
    height: 702px;
    overflow: hidden;
    background: var(--card-bg);
    font-family: "Caladea", Cambria, Georgia, serif;
    color: var(--ink);
  }
  .side-band {
    position: absolute;
    left: 0;
    top: 0;
    width: 1200px;
    height: 702px;
  }
  .line {
    position: absolute;
    left: 0;
    width: 1200px;
    margin: 0;
    text-align: center;
    line-height: 1;
    white-space: nowrap;
    font-weight: 400;
  }
  .company-name {
    top: 38px;
    font-size: 83px;
    color: var(--accent-blue);
    letter-spacing: 0.5px;
  }
  .company-address {
    top: 137px;
    font-size: 26.5px;
  }
  .header-rule {
    position: absolute;
    left: 123px;
    top: 186px;
    width: 947px;
    height: 3px;
    background: var(--accent-blue);
  }
  .person-name {
    top: 284px;
    font-size: 66px;
    color: var(--name-blue);
  }
  .person-title {
    top: 359px;
    font-size: 40px;
    color: var(--name-blue);
  }
  .contact {
    font-size: 31px;
  }
  .contact-mobile { top: 415px; }
  .contact-phone  { top: 454px; }
  .contact-email  { top: 494px; }
</style>
</head>
<body>
  <main class="card">
    <svg class="side-band" viewBox="0 0 1200 702" aria-hidden="true">
      <polygon points="0,0 28,0 243,702 0,702" fill="var(--accent-blue)"/>
      <line x1="28" y1="0" x2="243" y2="702" stroke="#c9e6f5" stroke-width="1.5" opacity="0.6"/>
    </svg>

    <h1 class="line company-name">BRAVO CONSTRUCTION</h1>
    <p class="line company-address">4318 Quarry Lane, San Bruno, California 94066</p>
    <div class="header-rule"></div>

    <h2 class="line person-name">Reginald Pottle</h2>
    <p class="line person-title">Contractor</p>

    <p class="line contact contact-mobile">mobile: (415) 555-0147</p>
    <p class="line contact contact-phone">phone: (650) 555-0183 ; Fax: (650) 555-0184</p>
    <p class="line contact contact-email">bravo@bravoconstruction.example</p>
  </main>
</body>
</html>
```